New design for our thank you cards *

We need Thank You card designs for our mortgage broking company "Copperleaf Lending". We have an existing design and need a revamp of these. We are a boutique broking firm and would like "thank you" cards to send to our clients who refer new clients.

We are a referral-based business, our success and longevity is inextricably linked to the advice and service we provide our clients and referral partners.

Industry/Entity Type

Mortgage Brokerage

Colors
0792cd
0255a3
3176b5
33a6d7
85acd3
85cae6
cee9f5
cedeed
ffffff

Requirements
Must have
• our logo on the front 7 thank you & print on the back

```html
<!DOCTYPE html>
<html lang="en">
<head>
<meta charset="utf-8">
<title>Copperleaf Lending – Thank You Card</title>
<link href="https://fonts.googleapis.com/css2?family=Great+Vibes&family=Jost:wght@500&display=swap" rel="stylesheet">
<style>
  :root {
    --sky-deep: #85cae6;
    --sky-mid: #cee9f5;
    --sky-soft: #cedeed;
    --white: #ffffff;
    --brand-blue: #0255a3;
    --bird-blue: #3176b5;
    --bird-light: #33a6d7;
    --ink: #111111;
    --backdrop: #eef3f8;
    --shadow: rgba(2, 40, 80, 0.18);
  }
  * { box-sizing: border-box; margin: 0; padding: 0; }
  html, body {
    width: 1200px; height: 1200px; overflow: hidden;
    background: var(--backdrop);
  }
  .sheet { position: relative; width: 1200px; height: 1200px; }

  .card {
    position: absolute;
    left: 230px;
    width: 740px; height: 523px;
    background:
      radial-gradient(ellipse 45% 35% at 8% 8%, rgba(133,202,230,0.9), transparent 70%),
      radial-gradient(ellipse 50% 30% at 70% 20%, rgba(206,233,245,0.9), transparent 70%),
      radial-gradient(ellipse 60% 25% at 35% 60%, rgba(206,233,245,0.8), transparent 70%),
      linear-gradient(to bottom, var(--sky-deep) 0%, var(--sky-mid) 40%, var(--sky-mid) 62%, var(--white) 80%, var(--white) 100%);
    box-shadow: 8px 10px 18px var(--shadow);
    overflow: hidden;
  }
  .card--front { top: 50px; }
  .card--back { top: 627px; }

  .greeting {
    position: absolute;
    left: 0; right: 0; top: 205px;
    text-align: center;
    font-family: "Great Vibes", cursive;
    font-weight: 400;
    font-size: 140px;
    line-height: 1;
    color: var(--ink);
    letter-spacing: 2px;
  }

  .bird {
    position: absolute;
    background: linear-gradient(135deg, var(--bird-light), var(--bird-blue) 55%, var(--brand-blue));
    border-radius: 50% 60% 40% 50%;
    opacity: 0.9;
  }
  .bird--perched { left: 215px; top: 118px; width: 80px; height: 56px; }
  .bird--flying { left: 505px; top: 130px; width: 80px; height: 46px; }

  .brand {
    position: absolute;
    left: 0; right: 0; bottom: 36px;
    display: flex; align-items: center; justify-content: center; gap: 14px;
    color: var(--brand-blue);
    font-family: "Jost", sans-serif;
    font-weight: 500;
  }
  .brand__mark {
    width: 68px; height: 68px;
    background: var(--brand-blue);
  }
  .brand__name { display: flex; flex-direction: column; line-height: 1.1; }
  .brand__name-top { font-size: 30px; letter-spacing: 1px; }
  .brand__name-bottom { font-size: 22px; letter-spacing: 8px; }
</style>
</head>
<body>
  <main class="sheet">
    <section class="card card--front" aria-label="Card front">
      <div class="bird bird--perched" role="img" aria-label="Blue bird perched above the lettering"></div>
      <div class="bird bird--flying" role="img" aria-label="Blue bird in flight"></div>
      <h1 class="greeting">Thank You</h1>
    </section>

    <section class="card card--back" aria-label="Card back">
      <div class="brand">
        <span class="brand__mark" aria-hidden="true"></span>
        <span class="brand__name">
          <span class="brand__name-top">COPPERLEAF</span>
          <span class="brand__name-bottom">LENDING</span>
        </span>
      </div>
    </section>
  </main>
</body>
</html>
```